Funeral Services Web Site

We need a website for a Funeral Services company. The choice of colors is free of charge. One Page Website with 8 sections. Menu: - Home - Our Services - Obituaries -> link to another page. - Our Shop - Funeral Monument - Funeral Contract - Contact Us

Target Market(s)

Every one need Funeral Services

Coding

Coded - Design and coding required

Number of Pages Required

2 page

Font styles to use
Sans Serif
Script

Colors

Designer to choose colors to be used in the design.

```html
<!DOCTYPE html>
<html lang="en">
<head>
<meta charset="utf-8">
<title>Verlaine-Moreau Funeral Homes</title>
<link href="https://fonts.googleapis.com/css2?family=Montserrat:wght@400;500;600;700&display=swap" rel="stylesheet">
<style>
:root{
  --brown:#6b3d10;
  --brown-dark:#4e2c0a;
  --cream:#f4f1e8;
  --white:#ffffff;
  --ink:#2a2a2a;
  --grey-nav:#ececec;
  --footer:#2c2c2c;
  --line:#c9b89c;
}
*{box-sizing:border-box;margin:0;padding:0}
html,body{width:1200px;height:4922px;overflow:hidden}
body{position:relative;font-family:"Montserrat",sans-serif;color:var(--ink);background:var(--white)}
.abs{position:absolute}
section,header,nav,footer{position:absolute;left:0;width:1200px;overflow:hidden}

.topbar{top:0;height:42px;background:var(--brown);color:#fff;font-size:13px}
.topbar .address{left:94px;top:13px;display:flex;align-items:center;gap:6px}
.topbar .social{right:98px;top:7px;display:flex;gap:10px}
.social span{display:block;width:28px;height:28px;border:1.5px solid #fff;border-radius:50%}

.site-header{top:42px;height:139px;background:var(--white)}
.contact-chip{display:flex;align-items:center;gap:14px;top:36px}
.contact-chip .ring{width:64px;height:64px;border:1.5px solid #8a7a66;border-radius:50%;display:flex;align-items:center;justify-content:center}
.contact-chip b{display:block;color:var(--brown);font-weight:500;font-size:17px;margin-bottom:8px}
.contact-chip small{font-size:17px;color:var(--ink)}
.brand{left:884px;top:16px;width:182px;height:112px;border:2px solid #8d7f6c;border-radius:6px;display:flex;align-items:center;justify-content:center;gap:8px;color:var(--brown);font-weight:600;font-size:17px}
.brand i{display:block;width:12px;height:12px;background:var(--brown)}

.main-nav{top:181px;height:69px;background:var(--grey-nav);border-top:2px solid #cfcfcf;display:flex;justify-content:center;gap:31px;padding-top:22px;font-size:17px;font-weight:500}
.main-nav a{color:var(--ink);text-decoration:none;height:30px}
.main-nav a.active{color:var(--brown);border-bottom:2px solid var(--brown)}

.hero{top:250px;height:644px}
.hero .photo{inset:0;background:radial-gradient(ellipse at 75% 30%,#8a8a7a 0%,#3c3d31 35%,#1f2118 70%,#141510 100%)}
.hero h1{left:92px;top:188px;color:#fff;font-size:48px;font-weight:600;line-height:1.2}
.hero h2{left:92px;top:254px;color:#fff;font-size:40px;font-weight:600}
.hero p{left:94px;top:320px;width:620px;color:#fff;font-size:20px;line-height:44px}

.welcome{top:894px;height:826px;background:var(--cream)}
.kicker{width:100%;text-align:center;font-size:26px}
.section-title{color:var(--brown);font-weight:700;font-size:36px}
.center{width:100%;text-align:center}
.divider{display:block;height:2px;width:70px;background:var(--line);margin:0 auto;position:relative}
.divider::after{content:"";position:absolute;left:29px;top:-5px;width:10px;height:10px;border:2px solid var(--line);transform:rotate(45deg);background:var(--cream)}
.photo-circle{border-radius:50%;border:8px solid #fff;box-shadow:0 8px 24px rgba(0,0,0,.25)}
.sub-title{color:var(--brown);font-weight:600;font-size:32px}
.body-text{font-size:16px;line-height:34px;text-align:justify}
.btn{display:flex;align-items:center;justify-content:center;background:var(--brown);color:#fff;font-weight:600;font-size:18px;box-shadow:2px 3px 4px rgba(0,0,0,.25)}

.services{top:1720px;height:630px;background:var(--white)}
.card{top:270px;width:320px;height:255px;border:2px solid var(--brown);text-align:center;padding-top:20px}
.card h3{color:var(--brown);font-size:14px;font-weight:600;line-height:27px;text-transform:uppercase;margin-top:10px}
.card p{font-size:11.5px;line-height:27px;padding:0 4px}
.card .more{color:var(--brown);font-size:14px;font-weight:600;margin-top:2px}

.shop{top:2350px;height:708px;background:var(--cream)}
.testimonials{top:3058px;height:649px;background:var(--white)}
.contact{top:3707px;height:746px;background:var(--cream)}
.field{height:40px;border:2px solid #8e8e8e;background:#fff;font-size:12px;padding:10px 14px;color:#555}

.site-footer{top:4453px;height:469px;background:var(--footer);color:#fff}
.footer-item{width:260px;text-align:center;font-size:17px;line-height:30px}
.footer-item .bubble{width:84px;height:84px;border-radius:50%;background:var(--brown);margin:0 auto 20px;display:flex;align-items:center;justify-content:center}
.footer-nav{top:330px;width:100%;text-align:center;font-size:16px;font-weight:500}
.copyright{top:378px;width:100%;text-align:center;font-size:15px}
.footer-social{top:410px;left:530px;display:flex;gap:6px}
.footer-social span{width:32px;height:32px;border:1.5px solid #fff;border-radius:50%}
</style>
</head>
<body>

<div class="topbar abs" style="position:absolute;left:0;width:1200px">
  <div class="address abs">
    <svg width="11" height="14" viewBox="0 0 11 14"><path d="M5.5 0A5.5 5.5 0 0 0 0 5.5C0 9.5 5.5 14 5.5 14S11 9.5 11 5.5A5.5 5.5 0 0 0 5.5 0zm0 7.7a2.2 2.2 0 1 1 0-4.4 2.2 2.2 0 0 1 0 4.4z" fill="#fff"/></svg>
    Rue des Tilleuls 14 - 5300 Andenne
  </div>
  <div class="social abs"><span></span><span></span><span></span><span></span></div>
</div>

<header class="site-header">
  <div class="contact-chip abs" style="left:110px">
    <div class="ring"><svg width="34" height="34" viewBox="0 0 34 34" fill="none" stroke="#6b3d10" stroke-width="1.5"><circle cx="17" cy="17" r="6"/><circle cx="17" cy="17" r="12"/></svg></div>
    <div><b>Send Flowers</b><small>Sympathies Via Website</small></div>
  </div>
  <div class="contact-chip abs" style="left:448px">
    <div class="ring"><svg width="30" height="30" viewBox="0 0 24 24" fill="none" stroke="#6b3d10" stroke-width="1.5"><path d="M5 3h4l2 5-3 2a12 12 0 0 0 6 6l2-3 5 2v4a2 2 0 0 1-2 2A17 17 0 0 1 3 5a2 2 0 0 1 2-2z"/></svg></div>
    <div><b>Immediate Need 24/7</b><small>081 / 42.19.63</small></div>
  </div>
  <div class="brand abs"><i></i>Verlaine-Moreau</div>
</header>

<nav class="main-nav">
  <a class="active">Home</a><a>Our Services</a><a>Obituaries</a><a>Our Shop</a><a>Funeral Monument</a><a>Funeral Contract</a><a>Contact Us</a>
</nav>

<section class="hero">
  <div class="photo abs" role="img" aria-label="Mourner in dark suit holding a white rose before lit candles"></div>
  <h1 class="abs">Verlaine-Moreau</h1>
  <h2 class="abs">Funeral Homes</h2>
  <p class="abs">Sed ut perspiciatis unde omnis iste natus error voluptatem accusantium doloremque laudantium explicabo.</p>
  <svg class="abs" style="left:0;bottom:0" width="1200" height="70" viewBox="0 0 1200 70" preserveAspectRatio="none">
    <path d="M0 30 Q300 -5 650 40 T1200 40 V70 H0Z" fill="#f4f1e8"/>
    <path d="M0 34 Q300 0 650 44 T1200 44" fill="none" stroke="#6b3d10" stroke-width="6"/>
  </svg>
</section>

<section class="welcome">
  <div class="kicker abs" style="top:100px">Welcome to</div>
  <div class="section-title center abs" style="top:140px">Verlaine-Moreau Funeral Homes</div>
  <div class="abs center" style="top:212px"><span class="divider"></span></div>
  <svg class="abs" style="left:44px;top:230px" width="480" height="420" viewBox="0 0 480 420"><path d="M90 40 A220 220 0 0 0 160 410" fill="none" stroke="#a88f6c" stroke-width="10" stroke-linecap="round"/><path d="M400 40 A220 220 0 0 1 330 410" fill="none" stroke="#c9b89c" stroke-width="6" stroke-linecap="round"/></svg>
  <div class="photo-circle abs" style="left:126px;top:268px;width:382px;height:382px;background:radial-gradient(circle at 50% 45%,#e6e3d8,#9a8a6a 55%,#4e4032)" role="img" aria-label="Funeral arrangement of white lilies in a vase"></div>
  <div class="sub-title abs" style="left:533px;top:258px">Our Funeral Home</div>
  <div class="body-text abs" style="left:538px;top:310px;width:562px">Located in the heart of Andenne, our funeral home is equipped with several private lounges that guarantee privacy and calm, as well as a cafeteria space.<br>In addition, we benefit from a complete infrastructure for the preparation and reception of the deceased: a treatment room adapted to thanatopraxy, a cold room, ...<br>Our funeral home has a large private parking opposite its main entrance, rue du Parvis.</div>
  <div class="btn abs" style="left:540px;top:602px;width:157px;height:46px">Read More</div>
  <svg class="abs" style="left:0;bottom:0" width="1200" height="90" viewBox="0 0 1200 90" preserveAspectRatio="none">
    <path d="M0 20 Q350 20 700 90 H0Z" fill="#fff"/><path d="M0 24 Q350 10 700 90 L1200 90 V90 H0Z" fill="#fff"/>
    <path d="M0 18 Q320 14 560 60" fill="none" stroke="#6b3d10" stroke-width="10"/>
  </svg>
</section>

<section class="services">
  <div class="section-title center abs" style="top:105px;font-size:34px">Our Services</div>
  <div class="abs center" style="top:165px"><span class="divider" style="background:#c9b89c"></span></div>
  <div class="abs center" style="top:190px;font-size:15px;line-height:33px">At vero eos et accusamus et iusto odio dignissimos ducimus qui blanditiis praesentium voluptatum<br>deleniti atque corrupti quos dolores et quas molestias excepturi sint</div>
  <svg class="abs" style="left:40px;top:385px" width="36" height="26" viewBox="0 0 36 26" fill="none" stroke="#6b3d10" stroke-width="2.5"><path d="M35 13H2M13 2 2 13l11 11"/></svg>
  <svg class="abs" style="left:1124px;top:385px" width="36" height="26" viewBox="0 0 36 26" fill="none" stroke="#6b3d10" stroke-width="2.5"><path d="M1 13h33M23 2l11 11-11 11"/></svg>
  <div class="card abs" style="left:90px">
    <svg width="60" height="44" viewBox="0 0 60 44"><rect x="0" y="10" width="10" height="24" fill="#6b3d10"/><rect x="50" y="10" width="10" height="24" fill="#6b3d10"/><path d="M12 14h12l8-6 10 6h6v18l-14 10L12 30z" fill="#6b3d10"/></svg>
    <h3>Personalized &amp; Dignified<br>Support from the First Moments</h3>
    <p>Verlaine-Moreau assist you and advise you when a loved one dies.</p>
    <div class="more">Read More →</div>
  </div>
  <div class="card abs" style="left:440px">
    <svg width="44" height="52" viewBox="0 0 44 52"><rect x="2" y="6" width="40" height="46" rx="4" fill="#6b3d10"/><rect x="14" y="0" width="16" height="10" rx="2" fill="#6b3d10"/><g fill="#fff"><rect x="10" y="18" width="4" height="4"/><rect x="18" y="19" width="16" height="2"/><rect x="10" y="28" width="4" height="4"/><rect x="18" y="29" width="16" height="2"/><rect x="10" y="38" width="4" height="4"/><rect x="18" y="39" width="16" height="2"/></g></svg>
    <h3>Assistance in All Administrativ<br>Procedures</h3>
    <p>Because the loss of a loved one causes a lot of steps, we help you accomplish them.</p>
    <div class="more">Read More →</div>
  </div>
  <div class="card abs" style="left:790px">
    <svg width="52" height="52" viewBox="0 0 52 52"><path d="M18 6 50 0v36h-6V10L24 14v30h-6z" fill="#6b3d10"/><ellipse cx="12" cy="44" rx="10" ry="7" fill="#6b3d10"/><ellipse cx="42" cy="38" rx="10" ry="7" fill="#6b3d10"/></svg>
    <h3>Offer Him His Song to Pay<br>Him a Last Tribute</h3>
    <p>Because a personalized song is an ideal way to pay tribute to a deceased, we work in partnership</p>
    <div class="more">Read More →</div>
  </div>
  <svg class="abs" style="left:0;bottom:0" width="1200" height="70" viewBox="0 0 1200 70" preserveAspectRatio="none">
    <path d="M0 40 Q600 -10 1200 60 V70 H0Z" fill="#f4f1e8"/>
    <path d="M620 14 Q950 20 1200 58" fill="none" stroke="#6b3d10" stroke-width="12"/>
  </svg>
</section>

<section class="shop">
  <div class="sub-title abs" style="left:88px;top:160px">Our Shop</div>
  <div class="abs" style="left:90px;top:226px"><span class="divider"></span></div>
  <div class="body-text abs" style="left:90px;top:253px;width:562px">Adjacent to our funeral home and accessible by Linden Street, our store offers a wide selection of silk flowers and funeral items.<br>Sed ut perspiciatis unde omnis iste natus error sit voluptatem accusantium doloremque laudantium, totam rem aperiam, eaque ipsa quae ab illo inventore veritatis et quasi architecto beatae vitae dicta sunt explicabo.</div>
  <div class="btn abs" style="left:90px;top:486px;width:186px;height:46px">Online Store</div>
  <svg class="abs" style="left:660px;top:120px" width="520" height="480" viewBox="0 0 520 480"><path d="M90 40 A250 250 0 0 0 140 460" fill="none" stroke="#a88f6c" stroke-width="10" stroke-linecap="round"/><path d="M440 40 A250 250 0 0 1 390 460" fill="none" stroke="#c9b89c" stroke-width="6" stroke-linecap="round"/></svg>
  <div class="photo-circle abs" style="left:707px;top:166px;width:424px;height:424px;background:radial-gradient(circle at 45% 55%,#c9a675,#a07a4a 40%,#ddd9d0 75%)" role="img" aria-label="Showroom with wooden caskets and funeral wreaths"></div>
  <svg class="abs" style="left:0;bottom:0" width="1200" height="70" viewBox="0 0 1200 70" preserveAspectRatio="none">
    <path d="M0 10 Q500 10 1200 70 H0Z" fill="#fff"/>
    <path d="M0 12 Q300 4 560 30" fill="none" stroke="#6b3d10" stroke-width="10"/>
  </svg>
</section>

<section class="testimonials">
  <div class="section-title center abs" style="top:185px;font-size:34px">Testimonials</div>
  <div class="abs center" style="top:250px"><span class="divider" style="background:#c9b89c"></span></div>
  <svg class="abs" style="left:573px;top:295px" width="54" height="44" viewBox="0 0 54 44"><path d="M0 44V26Q0 6 20 0l3 6Q12 12 12 22h10v22zM30 44V26Q30 6 50 0l3 6Q42 12 42 22h10v22z" fill="#2a2a2a"/></svg>
  <div class="abs center" style="top:352px;left:150px;width:900px;font-size:20px;line-height:36px">Sed ut perspiciatis unde omnis iste natus error sit voluptatem accusantium doloremque laudantium, totam rem aperiam, eaque ipsa quae ab illo inventore veritatis et quasi architecto beatae vitae dicta sunt explicabo.</div>
  <div class="abs center" style="top:477px;font-size:18px;font-weight:500">Anne Martin</div>
  <svg class="abs" style="left:66px;top:355px" width="68" height="44" viewBox="0 0 68 44" fill="none" stroke="#6b3d10" stroke-width="4"><path d="M66 22H4M22 3 3 22l19 19"/></svg>
  <svg class="abs" style="left:1066px;top:355px" width="68" height="44" viewBox="0 0 68 44" fill="none" stroke="#6b3d10" stroke-width="4"><path d="M2 22h62M46 3l19 19-19 19"/></svg>
  <svg class="abs" style="left:0;bottom:0" width="1200" height="70" viewBox="0 0 1200 70" preserveAspectRatio="none">
    <path d="M0 40 Q600 -10 1200 60 V70 H0Z" fill="#f4f1e8"/>
    <path d="M600 16 Q950 16 1200 50" fill="none" stroke="#6b3d10" stroke-width="12"/>
  </svg>
</section>

<section class="contact">
  <div class="section-title center abs" style="top:142px;font-size:34px">Contact Us</div>
  <div class="abs center" style="top:205px"><span class="divider"></span></div>
  <div class="abs center" style="top:247px;font-size:16px;line-height:36px">At vero eos et accusamus et iusto odio dignissimos ducimus qui blanditiis praesentium voluptatum deleniti<br>atque corrupti quos dolores et quas molestias excepturi sint occaecati cupiditate non provident</div>
  <div class="field abs" style="left:162px;top:348px;width:428px">&#128100; First Name</div>
  <div class="field abs" style="left:610px;top:348px;width:428px">&#128100; Last Name</div>
  <div class="field abs" style="left:162px;top:402px;width:428px">&#9632; Zipcode</div>
  <div class="field abs" style="left:162px;top:456px;width:428px">&#9993; Email Address</div>
  <div class="field abs" style="left:162px;top:510px;width:428px">&#9742; Phone Number</div>
  <div class="field abs" style="left:610px;top:402px;width:428px;height:148px">Message :</div>
  <div class="btn abs" style="left:520px;top:577px;width:152px;height:47px;font-size:17px">&#10148;&nbsp; SUBMIT</div>
</section>

<footer class="site-footer">
  <svg class="abs" style="left:0;top:0" width="1200" height="80" viewBox="0 0 1200 80" preserveAspectRatio="none">
    <path d="M0 0H1200V30Q800 80 500 40T0 30Z" fill="#f4f1e8"/>
    <path d="M480 46Q800 80 1200 34" fill="none" stroke="#6b3d10" stroke-width="10"/>
  </svg>
  <div class="footer-item abs" style="left:203px;top:135px">
    <div class="bubble"><svg width="30" height="38" viewBox="0 0 11 14"><path d="M5.5 1A4.5 4.5 0 0 0 1 5.5C1 9 5.5 13 5.5 13S10 9 10 5.5A4.5 4.5 0 0 0 5.5 1z" fill="none" stroke="#fff" stroke-width=".8"/><circle cx="5.5" cy="5.5" r="1.6" fill="none" stroke="#fff" stroke-width=".8"/></svg></div>
    Rue des Tilleuls 14<br>5300 Andenne
  </div>
  <div class="footer-item abs" style="left:462px;top:135px">
    <div class="bubble"><svg width="36" height="36" viewBox="0 0 24 24" fill="none" stroke="#fff" stroke-width="1.4"><path d="M5 3h4l2 5-3 2a12 12 0 0 0 6 6l2-3 5 2v4a2 2 0 0 1-2 2A17 17 0 0 1 3 5a2 2 0 0 1 2-2z"/></svg></div>
    Phone:<br>081 / 42.19.63
  </div>
  <div class="footer-item abs" style="left:721px;top:135px">
    <div class="bubble"><svg width="40" height="30" viewBox="0 0 40 30" fill="none" stroke="#fff" stroke-width="2"><rect x="1" y="1" width="38" height="28"/><path d="M1 1l19 16L39 1M1 29l14-14M39 29 25 15"/></svg></div>
    Email:<br>info@verlaine-moreau.be
  </div>
  <div class="footer-nav abs">Home &nbsp;|&nbsp; Our Services &nbsp;|&nbsp; Obituaries &nbsp;|&nbsp; Our Shop &nbsp;|&nbsp; Funeral Monument &nbsp;|&nbsp; Funeral Contract &nbsp;|&nbsp; Contact Us</div>
  <div class="copyright abs">© 2019 Company Name &nbsp;All right reserved</div>
  <div class="footer-social abs"><span></span><span></span><span></span><span></span></div>
</footer>

</body>
</html>
```